Business Card for a Floral & Decorating Business

I would like to take my current logo and create a better business card. I am looking for elegance as I am a florist and event decorator. My logo has multiple colour options. I like colours like green, purple, pink and orange, I think I would like a white card, open to black back ground. I want it to feel elegant and romantic. I like metallic lettering that maybe is indented in the paper, I also like glossy paper. I have a full logo already as well as a badge. I have attached both in multiple colours.m
Updates

Need extra days to review

Target Market(s)

Weddings, special events, floral customers

Industry/Entity Type

Floral and decorating

Contact Information for Business Card

Phone number, email, instagram, facebook, title, name, logo

Font styles to use
Script

Requirements
Nice to have
• Elegant

```html
<!DOCTYPE html>
<html lang="en">
<head>
<meta charset="utf-8">
<title>Marlow Everly – Business Card</title>
<link rel="stylesheet" href="https://fonts.googleapis.com/css2?family=Parisienne&family=Yellowtail&family=Cormorant+Garamond:wght@500&family=Roboto:wght@400&display=swap">
<style>
  :root {
    --backdrop: #c1c1c1;
    --paper: #ffffff;
    --wine: #8a2f4a;
    --wine-soft: #a3495f;
    --wine-card: #8e3d55;
    --wine-deep: #6f2a40;
    --blush: #f4e6ea;
  }
  * { box-sizing: border-box; margin: 0; padding: 0; }
  html, body {
    width: 671px; height: 1200px; overflow: hidden;
    background: var(--backdrop);
  }
  .sheet {
    position: relative; width: 671px; height: 1200px;
    display: flex; flex-direction: column; align-items: center; justify-content: center; gap: 62px;
  }
  .card {
    position: relative; width: 560px; height: 319px; overflow: hidden;
    box-shadow: 0 10px 26px rgba(0,0,0,.28);
  }
  .card--front { background: var(--paper); }
  .card--back { background: var(--wine-card); }

  .monogram-art {
    position: absolute; left: 0; top: 7px; width: 231px; height: 312px;
    background: linear-gradient(160deg, var(--blush) 0%, #e3b9c4 45%, var(--wine-soft) 100%);
    border-radius: 0 60px 60px 0;
  }
  .brand { position: absolute; text-align: center; }
  .brand__name {
    font-family: "Parisienne", cursive; font-weight: 400; white-space: nowrap; line-height: 1;
  }
  .brand__tagline {
    font-family: "Cormorant Garamond", serif; font-weight: 500;
    letter-spacing: .22em; text-transform: uppercase; line-height: 1;
  }
  .card--front .brand { left: 300px; top: 62px; width: 150px; color: var(--wine-soft); }
  .card--front .brand__name { font-size: 24px; }
  .card--front .brand__tagline { font-size: 5.5px; margin-top: 4px; }

  .services { position: absolute; left: 240px; top: 128px; width: 270px; text-align: center; color: var(--wine); }
  .services__title { font-family: "Yellowtail", cursive; font-size: 30px; line-height: 1; }
  .services__list {
    list-style: none; font-family: "Yellowtail", cursive; font-size: 14px;
    display: flex; flex-wrap: wrap; justify-content: center; column-gap: 24px; row-gap: 4px; margin-top: 8px;
  }
  .services__list li::before {
    content: ""; display: inline-block; width: 5px; height: 5px; border-radius: 50%;
    background: var(--wine-soft); margin-right: 8px; vertical-align: middle;
  }
  .services__list li:last-child { flex-basis: 100%; }

  .contact {
    position: absolute; left: 281px; top: 227px; list-style: none;
    font-family: "Roboto", sans-serif; font-size: 12.5px; color: var(--wine);
  }
  .contact li { display: flex; align-items: center; gap: 9px; height: 21px; }
  .contact svg { width: 11px; height: 11px; fill: var(--wine); }
  .social {
    position: absolute; left: 405px; top: 276px; display: flex; align-items: center; gap: 7px;
    font-family: "Roboto", sans-serif; font-size: 9px; color: var(--wine);
  }
  .social__rule { width: 40px; height: 1px; background: #b58595; }

  .card--back .brand { left: 180px; top: 148px; width: 200px; color: var(--blush); }
  .card--back .brand__name { font-size: 30px; }
  .card--back .brand__tagline { font-size: 6.5px; margin-top: 6px; }
  .faint-art { position: absolute; }
  .faint-art--right {
    left: 365px; top: 56px; width: 191px; height: 257px; border-radius: 0 80px 80px 0;
    background: linear-gradient(150deg, rgba(255,255,255,.06), rgba(111,42,64,.55));
  }
  .faint-art--corner {
    left: 0; top: 201px; width: 104px; height: 118px; border-top-right-radius: 60px;
    background: linear-gradient(200deg, rgba(255,255,255,.06), rgba(111,42,64,.35));
  }
</style>
</head>
<body>
<main class="sheet">
  <section class="card card--front" aria-label="Card front">
    <div class="monogram-art" role="img" aria-label="Large monogram letter entwined with line-drawn flowers and leaves"></div>
    <div class="brand">
      <p class="brand__name">marlow everly</p>
      <p class="brand__tagline">Decorating &amp; Florals.</p>
    </div>
    <div class="services">
      <h1 class="services__title">Floral and decorating</h1>
      <ul class="services__list">
        <li>Weddings</li>
        <li>special events</li>
        <li>floral customers</li>
      </ul>
    </div>
    <ul class="contact">
      <li>
        <svg viewBox="0 0 24 24" aria-hidden="true"><path d="M6.6 10.8a15.1 15.1 0 0 0 6.6 6.6l2.2-2.2c.3-.3.7-.4 1-.2 1.1.4 2.3.6 3.6.6.6 0 1 .4 1 1V20c0 .6-.4 1-1 1A17 17 0 0 1 3 4c0-.6.4-1 1-1h3.5c.6 0 1 .4 1 1 0 1.3.2 2.5.6 3.6.1.3 0 .7-.2 1z"/></svg>
        1234567890
      </li>
      <li>
        <svg viewBox="0 0 24 24" aria-hidden="true"><path d="M2 5h20v14H2z" fill="none"/><path d="M2 5h20v14H2V5zm2 2v.3l8 5.2 8-5.2V7H4zm16 2.6-8 5.2-8-5.2V17h16V9.6z"/></svg>
        hello@marloweverly.com
      </li>
    </ul>
    <div class="social">
      <span class="social__rule"></span>
      <span>@marloweverly</span>
    </div>
  </section>

  <section class="card card--back" aria-label="Card back">
    <div class="faint-art faint-art--right" role="img" aria-label="Faint tone-on-tone monogram with flowers"></div>
    <div class="faint-art faint-art--corner" role="img" aria-label="Faint tone-on-tone flowers and leaves"></div>
    <div class="brand">
      <p class="brand__name">marlow everly</p>
      <p class="brand__tagline">Decorating &amp; Florals.</p>
    </div>
  </section>
</main>
</body>
</html>
```